Business Card and Letterhead Design for Public Accounting Firm

Business card and letterhead design for a CPA Firm located in Orange County, CA. We're looking for a modern and professional design utilizing our existing logo. We'd like a clean "less is more" look, but also something that catches the eye. We provide a high level of service to our clients. Open to single or double sided business cards.

Additional info: color numbers on logo
Blue :
R 0
G 83
B 125

#00537D

Silver :

R 154
G 154
B 154

#9A9A9A

Target Market(s)

Businesses and individuals

Industry/Entity Type

Accounting

Contact Information for Business Card

Moss Whitfield & Danby LLP - 4827 Larkspur Vale Road, Irvine, CA 92614 - (949)731-2864 - mwdaccts.example

Font styles to use
Serif
Sans Serif
Other font styles liked:
• See font file uploaded

Colors
0054AA
0677BA
7BADD7
CADEEF
E8F1F8

Requirements
Nice to have
• Possibly use the font file provided which matches our logo, but adjust to be not in all caps

```html
<!DOCTYPE html>
<html lang="en">
<head>
<meta charset="utf-8">
<title>Moss Whitfield &amp; Danby LLP — Business Card</title>
<link rel="stylesheet" href="https://fonts.googleapis.com/css2?family=Cinzel:wght@400&family=Montserrat:wght@400;700&display=swap">
<style>
  :root {
    --page-bg: #2e2f31;
    --card-white: #fafafa;
    --card-white-edge: #e9e9e9;
    --brand-blue: #00537d;
    --brand-silver: #9a9a9a;
    --blue-deep: #08476f;
    --blue-light: #2589ab;
    --text-light: #ffffff;
    --silver-light: #c9d3da;
  }
  * { box-sizing: border-box; margin: 0; padding: 0; }
  html, body { width: 1200px; height: 1200px; overflow: hidden; }
  body {
    background: var(--page-bg);
    display: flex;
    flex-direction: column;
    align-items: center;
    justify-content: center;
    gap: 80px;
    font-family: "Montserrat", Arial, sans-serif;
  }
  .card {
    width: 700px;
    height: 400px;
    border-radius: 4px;
    box-shadow: 0 18px 40px rgba(0,0,0,0.45);
    position: relative;
  }

  /* Front */
  .card-front {
    background: linear-gradient(135deg, var(--card-white) 0%, var(--card-white-edge) 100%);
    display: flex;
    align-items: center;
    justify-content: center;
  }
  .brand-lockup { display: flex; align-items: center; gap: 22px; }
  .brand-square {
    width: 58px; height: 58px;
    background: var(--brand-blue);
  }
  .brand-divider {
    width: 1px; height: 90px;
    background: var(--brand-silver);
  }
  .brand-name {
    font-family: "Cinzel", Georgia, serif;
    font-weight: 400;
    color: var(--brand-blue);
    font-size: 30px;
    line-height: 1.15;
    letter-spacing: 3px;
  }

  /* Back */
  .card-back {
    background: radial-gradient(ellipse at 70% 30%, var(--blue-light) 0%, var(--blue-deep) 85%);
    color: var(--text-light);
  }
  .back-brand {
    position: absolute;
    left: 40px; top: 70px;
    display: flex; align-items: center; gap: 12px;
  }
  .back-brand .brand-square { width: 30px; height: 30px; background: var(--text-light); }
  .back-brand .brand-name {
    color: var(--silver-light);
    font-size: 15px;
    letter-spacing: 1.5px;
  }
  .back-divider {
    position: absolute;
    left: 300px; top: 130px;
    width: 1px; height: 210px;
    background: var(--text-light);
  }
  .contact {
    position: absolute;
    left: 330px; top: 135px;
  }
  .contact-firm {
    font-weight: 700;
    font-size: 23px;
    margin-bottom: 20px;
  }
  .contact-address {
    font-size: 16px;
    line-height: 1.4;
    margin-bottom: 8px;
  }
  .contact-line {
    display: flex; align-items: center; gap: 10px;
    font-size: 16px;
    line-height: 1.7;
  }
  .contact-line svg { width: 15px; height: 15px; flex: none; }
</style>
</head>
<body>

  <section class="card card-front" aria-label="Card front">
    <div class="brand-lockup">
      <div class="brand-square"></div>
      <div class="brand-divider"></div>
      <div class="brand-name">Moss Whitfield<br>&amp; Danby LLP</div>
    </div>
  </section>

  <section class="card card-back" aria-label="Card back">
    <div class="back-brand">
      <div class="brand-square"></div>
      <div class="brand-name">Moss Whitfield<br>&amp; Danby LLP</div>
    </div>
    <div class="back-divider"></div>
    <div class="contact">
      <p class="contact-firm">Moss Whitfield &amp; Danby LLP</p>
      <p class="contact-address">4827 Larkspur Vale Road,<br>Irvine, CA 92614</p>
      <p class="contact-line">
        <svg viewBox="0 0 24 24" fill="#ffffff" aria-hidden="true"><path d="M6.6 10.8a15.1 15.1 0 0 0 6.6 6.6l2.2-2.2a1 1 0 0 1 1-.25 11.4 11.4 0 0 0 3.6.57 1 1 0 0 1 1 1V20a1 1 0 0 1-1 1A17 17 0 0 1 3 4a1 1 0 0 1 1-1h3.5a1 1 0 0 1 1 1c0 1.25.2 2.45.57 3.57a1 1 0 0 1-.25 1z"/></svg>
        (949)731-2864
      </p>
      <p class="contact-line">
        <svg viewBox="0 0 24 24" fill="#ffffff" aria-hidden="true"><path d="M2 5h20v14H2z" opacity="0"/><path d="M2 5h20v14H2V5zm2 2v.4l8 5 8-5V7H4z"/></svg>
        cpas@mwdaccts.example
      </p>
      <p class="contact-line">
        <svg viewBox="0 0 24 24" fill="none" stroke="#ffffff" stroke-width="2" aria-hidden="true"><circle cx="12" cy="12" r="9"/><path d="M3 12h18M12 3c3 3.5 3 14.5 0 18M12 3c-3 3.5-3 14.5 0 18"/></svg>
        mwdaccts.example
      </p>
    </div>
  </section>

</body>
</html>
```